Marlo Tidy Yard Website

We need a website design for this new company. I've attached the company logo. This company is in the construction industry that provides general labor, maintenance and cleaning for construction sites. We want a clean and simple website that can be easy to navigate.

Target Market(s)

Construction industry

Industry/Entity Type

Construction

Number of Pages Required

2 page

Font styles to use
Sans Serif

```html
<!DOCTYPE html>
<html lang="en">
<head>
<meta charset="utf-8">
<title>Marlo Tidy Yard</title>
<link rel="stylesheet" href="https://fonts.googleapis.com/css2?family=Questrial&family=Montserrat:wght@600;700&family=Hind:wght@400&display=swap">
<style>
  :root {
    --navy: #0b0d7a;
    --ink: #111111;
    --orange: #f26a1b;
    --grey-text: #666666;
    --grey-soft: #8a8a8a;
    --panel: #e1e5e8;
    --dot: #0a7ec0;
    --footer: #2e4d8d;
    --white: #ffffff;
    --bar: #e4e6e7;
  }
  * { margin: 0; padding: 0; box-sizing: border-box; }
  html, body { width: 1200px; height: 1200px; overflow: hidden; }
  body {
    position: relative;
    font-family: "Questrial", Arial, sans-serif;
    color: var(--ink);
    background: linear-gradient(180deg, #f6f6f6 0%, #efefef 50%, #dedede 100%);
  }
  .top-strip { position: absolute; left: 0; top: 0; width: 1200px; height: 34px; background: #f4f4f4; }
  .site-header { position: absolute; left: 0; top: 34px; width: 1200px; height: 134px; background: var(--white); }
  .brand {
    position: absolute; left: 47px; top: 48px;
    display: flex; align-items: center; gap: 12px;
    font-family: "Montserrat", Arial, sans-serif; font-weight: 700;
    font-size: 30px; color: var(--navy); line-height: 1;
  }
  .brand-mark { width: 26px; height: 26px; background: var(--orange); }
  .tagline {
    position: absolute; right: 48px; top: 48px;
    font-family: "Montserrat", Arial, sans-serif; font-weight: 600;
    font-size: 15.5px; color: #444; letter-spacing: 0.2px;
  }
  .main-nav {
    position: absolute; right: 48px; top: 83px;
    display: flex; gap: 12px;
    font-family: "Montserrat", Arial, sans-serif; font-weight: 600;
    font-size: 16.5px; color: var(--navy);
  }
  .welcome {
    position: absolute; left: 0; top: 191px; width: 1200px; text-align: center;
    font-size: 33px; font-weight: 400; letter-spacing: 0.5px;
  }
  .welcome strong { font-family: "Montserrat", Arial, sans-serif; font-weight: 700; }
  .welcome .accent { color: var(--orange); }
  .welcome-sub {
    position: absolute; left: 0; top: 233px; width: 1200px; text-align: center;
    font-family: "Montserrat", Arial, sans-serif; font-weight: 600;
    font-size: 21px; color: var(--grey-soft);
  }
  .section-title {
    position: absolute; top: 296px;
    font-family: "Montserrat", Arial, sans-serif; font-weight: 600; font-size: 20px;
  }
  .services-title { left: 67px; width: 514px; padding-bottom: 4px; border-bottom: 1px solid #555; }
  .offers-title { right: 57px; }
  .slideshow { position: absolute; left: 67px; top: 333px; width: 521px; height: 295px; background: var(--panel); }
  .slideshow-label { position: absolute; left: 89px; top: 12px; font-size: 23px; color: #999; }
  .slide-image {
    position: absolute; left: 89px; top: 53px; width: 344px; height: 193px;
    background: linear-gradient(135deg, #8fc3ea 0%, #4b93cf 55%, #2a6fae 100%);
  }
  .slide-arrow { position: absolute; top: 121px; }
  .slide-arrow.prev { left: 44px; }
  .slide-arrow.next { left: 438px; }
  .slide-caption { position: absolute; left: 89px; top: 255px; font-size: 26px; }
  .offers-list {
    position: absolute; left: 800px; top: 333px; width: 353px; height: 295px;
    background: var(--panel); list-style: none; padding-top: 6px;
    font-family: "Hind", Arial, sans-serif; font-size: 21px; color: var(--grey-text);
  }
  .offers-list li { height: 35.3px; line-height: 35.3px; padding-left: 51px; position: relative; }
  .offers-list li::before {
    content: ""; position: absolute; left: 17px; top: 13px; width: 10px; height: 10px;
    border-radius: 50%; background: radial-gradient(circle at 35% 35%, #7bc0ec, var(--dot));
  }
  .how-title {
    position: absolute; left: 0; top: 670px; width: 1200px; text-align: center;
    font-family: "Montserrat", Arial, sans-serif; font-weight: 600; font-size: 27px; color: var(--grey-text);
  }
  .step { position: absolute; top: 718px; }
  .step-dot { position: absolute; top: 0; width: 100px; height: 100px; border-radius: 50%; background: var(--dot); }
  .step-title {
    position: absolute; top: 116px; white-space: nowrap;
    font-family: "Montserrat", Arial, sans-serif; font-weight: 600; font-size: 20.5px;
  }
  .step-text { position: absolute; top: 153px; width: 320px; font-size: 21px; line-height: 26px; }
  .step-1 { left: 107px; } .step-1 .step-dot { left: 62px; }
  .step-2 { left: 480px; } .step-2 .step-dot { left: 71px; }
  .step-3 { left: 847px; } .step-3 .step-dot { left: 86px; }
  .site-footer { position: absolute; left: 0; top: 969px; width: 1200px; height: 199px; background: var(--footer); color: var(--white); }
  .footer-col { position: absolute; top: 26px; }
  .footer-col h3 { font-family: "Montserrat", Arial, sans-serif; font-weight: 700; font-size: 15.5px; margin-bottom: 16px; }
  .footer-col ul { list-style: none; font-family: "Hind", Arial, sans-serif; font-size: 12.5px; line-height: 21px; }
  .col-services { left: 49px; } .col-services ul { font-size: 11.5px; padding-left: 2px; }
  .col-social { left: 359px; }
  .col-links { left: 667px; }
  .col-account { left: 976px; top: 62px; }
  .social-row { display: flex; gap: 24px; margin: 2px 0 0 1px; }
  .social-dot { width: 26px; height: 26px; border-radius: 50%; background: var(--white); box-shadow: 0 2px 6px rgba(255,255,255,0.45); }
  .contact-lines { margin-top: 32px; font-family: "Hind", Arial, sans-serif; font-size: 13px; line-height: 21px; }
  .bottom-bar {
    position: absolute; left: 0; top: 1168px; width: 1200px; height: 32px; background: var(--bar);
    text-align: center; line-height: 32px; font-family: "Hind", Arial, sans-serif; font-size: 12px; color: #222;
  }
</style>
</head>
<body>
  <div class="top-strip"></div>
  <header class="site-header">
    <div class="brand"><span class="brand-mark"></span>Marlo Tidy Yard</div>
    <div class="tagline">CONSTRUCTION CLEAN UP GENERAL LABOR MAINTENANCE</div>
    <nav class="main-nav">
      <span>HOME</span><span>ABOUT</span><span>SERVICES</span><span>PROJECTS</span><span>CONTACT</span>
    </nav>
  </header>

  <h1 class="welcome">WELCOME TO <strong>MARLO</strong> <strong class="accent">TIDY YARD</strong></h1>
  <p class="welcome-sub">CLEANING SERVICES LONDON</p>

  <h2 class="section-title services-title">SPECIALIST CLEANING SERVICES</h2>
  <h2 class="section-title offers-title">MARLO OFFERS OUR CUSTOMERS:</h2>

  <section class="slideshow">
    <div class="slideshow-label">DYNAMIC SLIDESHOW</div>
    <div class="slide-image" role="img" aria-label="Photo of a worker abseiling down a glass office facade cleaning windows"></div>
    <svg class="slide-arrow prev" width="40" height="72" viewBox="0 0 40 72"><polyline points="36,4 4,36 36,68" fill="none" stroke="#111" stroke-width="3"/></svg>
    <svg class="slide-arrow next" width="40" height="72" viewBox="0 0 40 72"><polyline points="4,4 36,36 4,68" fill="none" stroke="#111" stroke-width="3"/></svg>
    <div class="slide-caption">Class Cleaning</div>
  </section>

  <ul class="offers-list">
    <li>The option of Green Cleaning</li>
    <li>A dedicated workforce</li>
    <li>24/7/365 Customer Care Center</li>
    <li>Web-based work order system</li>
    <li>SnapShot Inspection services</li>
    <li>Full-service janitorial cleaning</li>
    <li>Special services</li>
    <li>National strength</li>
  </ul>

  <h2 class="how-title">HOW IT WORKS</h2>
  <div class="step step-1">
    <div class="step-dot"></div>
    <h3 class="step-title">BOOK A DAY &amp; TIME</h3>
    <p class="step-text">Tell us what you need<br>and we'll do the rest</p>
  </div>
  <div class="step step-2">
    <div class="step-dot"></div>
    <h3 class="step-title">WE SEND YOU A CLEANER</h3>
    <p class="step-text">We handle everything and<br>sort all of the details for you</p>
  </div>
  <div class="step step-3">
    <div class="step-dot"></div>
    <h3 class="step-title">YOUR PROPERTY IS CLEANED</h3>
    <p class="step-text">You can decide to have a o<br>ne off or regular clean</p>
  </div>

  <footer class="site-footer">
    <div class="footer-col col-services">
      <h3>MAINTENANCE SERVICES</h3>
      <ul>
        <li>Exterior window cleaning</li>
        <li>High window cleaning</li>
        <li>Interior window cleaning</li>
        <li>Grout restoration</li>
        <li>Millwork maintenance</li>
        <li>Carpet cleaning</li>
      </ul>
    </div>
    <div class="footer-col col-social">
      <h3>STAY CONNECTED</h3>
      <div class="social-row">
        <span class="social-dot"></span><span class="social-dot"></span><span class="social-dot"></span><span class="social-dot"></span>
      </div>
      <div class="contact-lines">01632 96 04 17<br>hello@marlotidyyard.example</div>
    </div>
    <div class="footer-col col-links">
      <h3>STAY CONNECTED</h3>
      <ul>
        <li>Help Page</li>
        <li>FAQ</li>
        <li>Sitemap</li>
        <li>Accessibility</li>
        <li>Privacy &amp; cookies</li>
        <li>Terms and Conditions</li>
      </ul>
    </div>
    <div class="footer-col col-account">
      <ul>
        <li>Login</li>
        <li>Booking page</li>
      </ul>
    </div>
  </footer>
  <div class="bottom-bar">© 2019 Marlo Tidy Yard</div>
</body>
</html>
```